Sail Us to Harbourlight.co.nz .... Tourism business providing guided tours.

Design and build a website for our new company. The company is one where we take tourists to beautiful places for a fully guided tour for 2 weeks. Tours can follow our itinerary or be tailored to suit individual clients. .... Let us tell you a little of what we are about ....
Flying our clients to paradise for a ‘ Tailor Made ‘ tour or one where we organise everything and use our combined knowledge of more than 50 years experience in Indonesia where we travel to some of the places that are not well known on the tourist map, places that are often off the beaten track of tourists but that are spectacularly beautiful.
Our team .... Lucas Montrose (Ex Iron Fern), Gareth Thorne, Marisa Thorne & Sekar Purnama have reached a stage in life where making money is not essential but enjoying life is. We all have a passion to help others experience what we have when we travel to our paradise whether that is Indonesia, where we are starting our tours then we will be working on Thailand, Malaysia, Vietnam or New Zealand along with a number of other countries.
The experience of the ‘ Ladies ‘ in the team who are both native to the country along with my experience in the Film Production business where I have produced a number of documentaries on travelling through Indonesia and show casing the spectacular scenery there gives our clients access to what they will experience through my Vid Harbor channel. …. https://www.vidharbor.example/user/gthornefilm/videos
We claim to be the only tour company that produces documentaries on what our guests can expect to experience on their travels with us. All trips are personally guided with one of our team and we can also Taylor make trips where groups can be personally guided by the Ex Iron Fern in our team Lucas Montrose. Further to that we film and produce a Video of your trip as it happens ... that is something special that you get to keep and show friends & family.
To top that off we have Lucas Montrose on board who can call on his experience of travelling with the Iron Fern team but also his position as entertainment director for the IF’S on tour.
Lucas also has a vast experience as a host where he has hosted celebrities and entertained large companies which included Varnex the French aircraft maker and Heron Journal in Bali.
He has also been involved with organising events and hosting guests for the Prince and Princess of Monaco.
Sekar has a Batchelor degree in marketing and management and worked in the hotel industry and also runs Staynook villas where she is working on expanding that to the next level in Bali.
By chance we had been working on forming such a tour company individually and when we all realised this it was obvious we needed to form a company where we can call on our individual strengths.
The company will soon introduce other celebrity guides for our tours that will open opportunities for other ex players of International teams that are looking for opportunities when their playing careers finish.
What really stands out in Indonesia is the people - we consider they are the friendliest of all the countries we have travelled through. As a film maker I experience this throughout the country. When I intrude on peoples life and culture I am invariably met with a response that is so touching. The people of Indonesia are so proud of their way of life and equally as proud that I show such interest in their life. Our target market is clients that want to experience what we want to experience.
Bali is one part of our trip but the Island of Bali and the 17,200 other islands that make up the Indonesian Archipelago are what we have so much experience in travelling thru (some of - not all .... Yet?) and that is what makes our paradise the aim of the tours.
The company is currently being formed along with our Logo, brochures and a comprehensive website that will be online in a couple of weeks. Further to that and what in fact will be the main promotional tool for our company, we have a number of documentaries that will showcase ‘ Radiant Nusantara ‘ from the air and the ground that have been produced and are under production by our own in-house Film production company Quietcoastline pictures.
Links :https://www.vidharbor.example/watch?v=Qp7rTn2LmZk&feature=share&ref=Kd83JsPqWnRtYxLmZa92HvBcUeFgNiOpTsQwErTy&app=desktop
Our contact details :
‘ Sail Us to Harbourlight ‘ sailustoharbourlightnz@quillmail.example
Gareth & Marisa Thorne oakbarn_decor@kowhainet.example
Lucas Montrose: lmontrose17@quillmail.example

Target Market(s)

Older people with money to spend on holidays in Paradise .... We are adamant, at this stage that we are looking at the higher end of the market so that our tours are unique and not a crowded tour where all follow the leader. We want to retain the flexibility so that at the start of each day we can offer alternatives to what is on the itinerary. For example some of the group could go rafting and the ladies may prefer to go in another direction and to facilitate this we will have more than one vehicle on hand to do this.

Industry/Entity Type

Tourism

Coding

Coded - Design and coding required

Number of Pages Required

5+ page

Font styles to use
Serif

Colors
0792cd
85cae6
00a990

Requirements
Must have
• Buttons so prospective clients can book and pay for a trip
• Links to various Documentaries we have on out Vid Harbor Page .... Quietcoastline Pictures
• Contact details for each of the partners
Nice to have
• A similar site to https://www.tulipmarrtravel.example/premium-journeys/

```html
<!DOCTYPE html>
<html lang="en">
<head>
<meta charset="utf-8">
<title>Sail Us to Harbourlight – Tours to Beautiful Places</title>
<link href="https://fonts.googleapis.com/css2?family=Arimo:wght@400;700&family=Marcellus&display=swap" rel="stylesheet">
<style>
:root{
  --blue:#0792cd;
  --sky:#85cae6;
  --green:#00a990;
  --navy:#0b2a6e;
  --ink:#222;
  --muted:#777;
  --grey:#efefef;
  --white:#fff;
}
*{box-sizing:border-box;margin:0;padding:0}
html,body{width:1200px;height:5341px;overflow:hidden}
body{position:relative;background:var(--white);font-family:"Arimo",Arial,sans-serif;color:var(--ink)}
.abs{position:absolute}
.photo{position:absolute;display:block}

/* header */
.brand{left:89px;top:22px;display:flex;align-items:center;gap:12px}
.brand-mark{width:42px;height:42px;border-radius:50%;background:var(--navy)}
.brand-name{font-weight:700;font-size:17px;color:var(--navy);letter-spacing:.5px;line-height:1.15;width:200px}
.phone{right:92px;top:12px;color:var(--blue);font-weight:700;font-size:20px;display:flex;align-items:center;gap:8px}
.socials{display:flex;gap:8px}
.socials span{width:30px;height:30px;border-radius:50%;display:block}
.head-social{left:665px;top:62px}
.s1{background:#3b5998}.s2{background:#e52d27}.s3{background:#dd4b39}.s4{background:#1da1f2}.s5{background:#3f729b}
.btn-book{left:942px;top:56px;width:168px;height:44px;border-radius:22px;background:var(--navy);color:#fff;font-weight:700;font-size:16px;display:flex;align-items:center;justify-content:center}
.nav{left:0;top:125px;width:1200px;height:53px;background:var(--green);display:flex;justify-content:space-between;align-items:center;padding:0 85px}
.nav a{color:#fff;text-decoration:none;font-weight:700;font-size:14px;letter-spacing:.3px}

/* hero */
.hero{left:0;top:178px;width:1200px;height:622px;overflow:hidden}
.hero-photo{left:0;top:0;width:1200px;height:622px;background:radial-gradient(ellipse at 50% 55%,#d9cfa8 0,#4fb4c8 18%,#1578a8 45%,#0e4f85 100%)}
.hero-title{left:0;top:108px;width:1200px;text-align:center;color:#fff;font-weight:700;font-size:90px;text-shadow:0 2px 6px rgba(0,0,0,.3)}
.hero-sub{left:0;top:212px;width:1200px;text-align:center;color:#fff;font-size:29px;letter-spacing:3px}
.search{left:231px;top:268px;width:737px;height:60px;border-radius:30px;background:#fff;display:flex;align-items:center;padding-left:32px;color:#999;font-size:17px}
.search-btn{position:absolute;right:4px;top:4px;width:172px;height:52px;border-radius:26px;background:var(--green);color:#fff;font-size:22px;display:flex;align-items:center;justify-content:center;border:3px solid #fff}
.dots{left:0;top:386px;width:1200px;display:flex;justify-content:center;gap:18px}
.dots span{width:22px;height:22px;border-radius:50%;border:3px solid #fff}
.dots span:first-child{background:#fff}
.hero-curve{left:0;top:0;width:1200px;height:622px}

/* section headings */
.sec-title{left:0;width:1200px;text-align:center;font-family:"Marcellus",Georgia,serif;font-size:46px;color:var(--ink)}
.sec-rule{width:52px;height:8px;border-top:3px solid var(--green);border-bottom:3px solid var(--green);left:574px}

/* destination */
.tile{position:absolute}
.btn{position:absolute;height:54px;border-radius:27px;color:#fff;font-size:17px;display:flex;align-items:center;justify-content:center}
.btn-green{background:var(--green)}
.btn-blue{background:var(--blue)}

/* documentary */
.doc-title{color:#fff}
.doc-rule{border-color:var(--sky)}
.video{position:absolute;width:431px;height:271px;box-shadow:0 4px 10px rgba(0,0,0,.3)}
.play{position:absolute;left:190px;top:110px;width:52px;height:52px;border-radius:50%;border:3px solid rgba(255,255,255,.8)}
.play::after{content:"";position:absolute;left:18px;top:12px;border-left:17px solid rgba(255,255,255,.85);border-top:11px solid transparent;border-bottom:11px solid transparent}
.video-cap{position:absolute;color:#fff;font-size:26px}

/* team */
.member{position:absolute;top:2730px;width:236px;height:340px;text-align:center}
.ring{position:absolute;left:0;top:60px;width:236px;height:236px;border-radius:50%;border:4px solid var(--blue);border-top-color:transparent;border-right-color:var(--blue)}
.portrait{position:absolute;left:14px;top:10px;width:208px;height:208px;border-radius:50%;background:linear-gradient(160deg,#c9a58a,#7a5a48);border:4px solid #fff;box-shadow:0 2px 8px rgba(0,0,0,.2)}
.m-name{position:absolute;top:238px;left:0;width:236px;font-size:17px;color:var(--ink)}
.m-mail{position:absolute;top:262px;left:0;width:236px;font-size:11px;color:var(--muted)}
.m-social{position:absolute;top:298px;left:0;width:236px;display:flex;justify-content:center;gap:10px}
.m-social span{width:10px;height:10px;border-radius:50%;background:var(--blue)}

/* gallery */
.gallery-bg{left:0;top:3204px;width:1200px;height:837px;background:var(--grey)}
.g{position:absolute;width:250px;height:238px}

/* feedback */
.card{position:absolute;top:4261px;width:330px;height:303px;background:#fff;box-shadow:0 3px 14px rgba(0,0,0,.15);padding:0 28px}
.quote{position:absolute;left:28px;top:16px;width:46px;height:46px;background:var(--blue);color:#fff;font-family:"Marcellus",Georgia,serif;font-size:40px;line-height:58px;text-align:center}
.c-title{position:absolute;left:28px;top:86px;font-weight:700;font-size:17px}
.c-text{position:absolute;left:28px;top:120px;width:274px;font-size:13px;line-height:22px;color:#666}
.c-foot{position:absolute;left:28px;top:243px;width:274px;display:flex;align-items:center;gap:12px}
.avatar{width:36px;height:36px;border-radius:50%;background:linear-gradient(160deg,#c79b7f,#6e4f3f)}
.c-name{color:var(--green);font-size:22px;flex:1}
.c-date{font-size:12px;color:#444}

/* footer */
.footer-curve{left:0;top:4660px;width:1200px;height:681px}
.f-brand{left:0;top:4815px;width:1200px;display:flex;justify-content:center;align-items:center;gap:12px}
.f-brand .brand-mark{background:#fff;width:38px;height:38px}
.f-brand .brand-name{color:#fff;width:auto}
.f-h{position:absolute;color:#fff;font-family:"Marcellus",Georgia,serif;font-size:27px}
.f-text{position:absolute;color:#dfe6f5;font-size:13px;line-height:22px}
.email-field{left:148px;top:5076px;width:306px;height:42px;border-radius:21px;background:#fff;color:#999;font-size:12px;padding-left:20px;display:flex;align-items:center}
.btn-signup{left:148px;top:5132px;width:130px;height:40px;border-radius:20px;background:var(--green);color:#fff;font-weight:700;font-size:14px;display:flex;align-items:center;justify-content:center}
.links{left:562px;top:5010px;list-style:none;color:#fff;font-size:14px;line-height:30px}
.contact-row{position:absolute;left:833px;display:flex;gap:14px;color:#fff;font-size:13px;line-height:19px}
.c-icon{width:30px;height:30px;background:var(--green);border-radius:4px;flex:none;display:flex;align-items:center;justify-content:center}
.foot-social{left:0;top:5266px;width:1200px;display:flex;justify-content:center;gap:18px}
.foot-social span{width:34px;height:34px;border-radius:50%;display:block}
.copy{left:0;top:5312px;width:1200px;text-align:center;color:#dfe6f5;font-size:12px}
</style>
</head>
<body>

<!-- header -->
<div class="abs brand"><span class="brand-mark"></span><span class="brand-name">SAIL US TO HARBOURLIGHT</span></div>
<div class="abs phone">
  <svg width="20" height="20" viewBox="0 0 24 24"><path fill="#0792cd" d="M6.6 10.8a15 15 0 0 0 6.6 6.6l2.2-2.2a1 1 0 0 1 1-.25 11.4 11.4 0 0 0 3.6.57 1 1 0 0 1 1 1V20a1 1 0 0 1-1 1A17 17 0 0 1 3 4a1 1 0 0 1 1-1h3.5a1 1 0 0 1 1 1c0 1.25.2 2.45.57 3.6a1 1 0 0 1-.25 1z"/></svg>
  +1 555 0142 7730
</div>
<div class="abs socials head-social"><span class="s1"></span><span class="s2"></span><span class="s3"></span><span class="s4"></span><span class="s5"></span></div>
<div class="abs btn-book">Book Now</div>
<nav class="abs nav">
  <a>DESTINATIONS</a><a>TOURS</a><a>DOCUMENTARY</a><a>SPECIAL OFFERS</a><a>ABOUT US</a><a>BEFORE YOU GO</a><a>REVIEWS</a>
</nav>

<!-- hero -->
<section class="abs hero">
  <div class="photo hero-photo" role="img" aria-label="Aerial view of a small tropical island with white sand ringed by turquoise sea"></div>
  <svg class="abs hero-curve" viewBox="0 0 1200 622" preserveAspectRatio="none">
    <path fill="#0792cd" d="M640 600 C900 560 1080 520 1200 470 L1200 540 C1050 580 850 605 640 600 Z"/>
    <path fill="#fff" d="M0 470 C250 560 480 620 700 610 C900 600 1080 560 1200 530 L1200 622 L0 622 Z"/>
  </svg>
  <div class="abs hero-title">Sail Us To Harbourlight</div>
  <div class="abs hero-sub">TOURS TO BEAUTIFUL PLACES</div>
  <div class="abs search">Where Do You Want To Explore ?<span class="search-btn">Search</span></div>
  <div class="abs dots"><span></span><span></span><span></span><span></span></div>
</section>

<!-- destination -->
<h2 class="abs sec-title" style="top:918px">Destination</h2>
<div class="abs sec-rule" style="top:988px"></div>
<div class="tile" style="left:89px;top:1050px;width:406px;height:240px;background:linear-gradient(150deg,#bfe3e6,#5aa4b3 60%,#3b7e8a)" role="img" aria-label="Aerial view of a jetty over clear shallow water"></div>
<div class="tile" style="left:89px;top:1306px;width:406px;height:296px;background:linear-gradient(180deg,#b9d2df 0,#c9d6d8 45%,#d9cbb0 60%,#c4b597 100%)" role="img" aria-label="Riders on horseback along a wide beach"></div>
<div class="tile" style="left:506px;top:1050px;width:309px;height:552px;background:linear-gradient(180deg,#c9d7e3 0,#8b7f72 35%,#6f665c 70%,#9d9380 100%)" role="img" aria-label="Travellers in front of a tall stone temple"></div>
<div class="tile" style="left:830px;top:1050px;width:277px;height:302px;background:linear-gradient(180deg,#b8c9b0,#6e8d6a 55%,#4a5a44)" role="img" aria-label="Traveller beside an island welcome sign"></div>
<div class="tile" style="left:830px;top:1366px;width:277px;height:236px;background:linear-gradient(180deg,#9fc3e0,#c9b79e 55%,#6a5a4e)" role="img" aria-label="Couple in sun hats smiling by the water"></div>
<div class="btn btn-green" style="left:413px;top:1664px;width:160px">VIEW ALL</div>
<div class="btn btn-blue" style="left:591px;top:1664px;width:196px">PAY FOR A TRIP</div>

<!-- documentary -->
<svg class="abs" style="left:0;top:1740px" width="1200" height="890" viewBox="0 0 1200 890" preserveAspectRatio="none">
  <path fill="#0792cd" d="M0 95 C250 150 600 165 1200 110 L1200 700 C800 690 400 720 0 770 Z"/>
  <path fill="#00a990" d="M380 150 C700 140 1000 90 1200 0 L1200 110 C900 145 650 160 380 150 Z"/>
  <path fill="#00a990" d="M0 770 C350 715 750 695 1200 700 L1200 715 C800 720 400 770 0 880 Z"/>
</svg>
<h2 class="abs sec-title doc-title" style="top:1970px">Our Documentary</h2>
<div class="abs sec-rule doc-rule" style="top:2040px"></div>
<div class="video" style="left:128px;top:2093px;background:linear-gradient(135deg,#2a4f7a,#6b6fa0 50%,#7a5a48)" role="img" aria-label="Documentary still of two presenters on a boat">
  <span class="play"></span></div>
<div class="video-cap" style="left:128px;top:2370px">Radiant Nusantara</div>
<div class="video" style="left:641px;top:2093px;background:linear-gradient(135deg,#3d2e24,#7a5a3e 50%,#a88a62)" role="img" aria-label="Documentary still of a group sharing a meal">
  <span class="play"></span></div>
<div class="video-cap" style="left:641px;top:2370px">Quietcoastline pictures</div>

<!-- team -->
<h2 class="abs sec-title" style="top:2638px">Our Team</h2>
<div class="abs sec-rule" style="top:2708px"></div>
<div class="member" style="left:88px"><span class="ring"></span><span class="portrait" role="img" aria-label="Portrait of Lucas Montrose"></span>
  <div class="m-name">Lucas Montrose</div><div class="m-mail">lmontrose17@quillmail.example</div>
  <div class="m-social"><span></span><span></span><span></span><span></span></div></div>
<div class="member" style="left:348px"><span class="ring"></span><span class="portrait" role="img" aria-label="Portrait of Gareth Thorne"></span>
  <div class="m-name">Gareth Thorne</div><div class="m-mail">oakbarn_decor@kowhainet.example</div>
  <div class="m-social"><span></span><span></span><span></span><span></span></div></div>
<div class="member" style="left:612px"><span class="ring"></span><span class="portrait" role="img" aria-label="Portrait of Marisa Thorne"></span>
  <div class="m-name">Marisa Thorne</div><div class="m-mail">oakbarn_decor@kowhainet.example</div>
  <div class="m-social"><span></span><span></span><span></span><span></span></div></div>
<div class="member" style="left:872px"><span class="ring"></span><span class="portrait" role="img" aria-label="Portrait of Sekar Purnama"></span>
  <div class="m-name">Sekar Purnama</div><div class="m-mail">Lorem ipsum</div>
  <div class="m-social"><span></span><span></span><span></span><span></span></div></div>

<!-- gallery -->
<div class="abs gallery-bg"></div>
<h2 class="abs sec-title" style="top:3320px">Gallery</h2>
<div class="abs sec-rule" style="top:3390px"></div>
<div class="g" style="left:89px;top:3432px;background:linear-gradient(180deg,#8fb8d8,#e3ebf0 40%,#3f7a5a 70%,#2a6a8a)" role="img" aria-label="Coastline under billowing clouds"></div>
<div class="g" style="left:345px;top:3432px;background:linear-gradient(135deg,#1d6f8e,#46b3c0 50%,#2e8a6c)" role="img" aria-label="Aerial view of islands in turquoise water"></div>
<div class="g" style="left:601px;top:3432px;background:linear-gradient(180deg,#bcd8e6,#d8c8a8 55%,#c7b18a)" role="img" aria-label="Sunbathers on a sandy beach"></div>
<div class="g" style="left:857px;top:3432px;background:linear-gradient(180deg,#e7a66b,#c07a58 45%,#3c3a4a)" role="img" aria-label="Friends jumping on the beach at sunset"></div>
<div class="g" style="left:89px;top:3678px;background:linear-gradient(180deg,#1f6d90,#2a8fa6 50%,#5a8c6c)" role="img" aria-label="Coral reef under clear water"></div>
<div class="g" style="left:345px;top:3678px;background:linear-gradient(180deg,#a9c8dc,#7a6a5a 55%,#4f6a7a)" role="img" aria-label="Traveller at a waterfront village"></div>
<div class="g" style="left:601px;top:3678px;background:linear-gradient(180deg,#4a3a30,#8a6a4a 50%,#b98a5a)" role="img" aria-label="Colourful market stalls"></div>
<div class="g" style="left:857px;top:3678px;background:linear-gradient(180deg,#9fb5c5,#4f7a6a 50%,#2d5f70)" role="img" aria-label="Karst islands rising from a lagoon"></div>

<!-- feedback -->
<h2 class="abs sec-title" style="top:4160px">Customer Feedback</h2>
<div class="abs sec-rule" style="top:4230px"></div>
<div class="card" style="left:82px"><span class="quote">“</span><div class="c-title">Perspiciatis</div>
  <p class="c-text">At vero eos et accusamus et iusto odio mos mus qui blanditiis praesentium tatum deleniti atque corrupti quos do.</p>
  <div class="c-foot"><span class="avatar" role="img" aria-label="Reviewer photo"></span><span class="c-name">Tessa Vale</span><span class="c-date">28 Feb 2019</span></div></div>
<div class="card" style="left:438px"><span class="quote">“</span><div class="c-title">Perspiciatis</div>
  <p class="c-text">At vero eos et accusamus et iusto odio mos mus qui blanditiis praesentium tatum deleniti atque corrupti quos do.</p>
  <div class="c-foot"><span class="avatar" role="img" aria-label="Reviewer photo"></span><span class="c-name">Tessa Vale</span><span class="c-date">28 Feb 2019</span></div></div>
<div class="card" style="left:794px"><span class="quote">“</span><div class="c-title">Perspiciatis</div>
  <p class="c-text">At vero eos et accusamus et iusto odio mos mus qui blanditiis praesentium tatum deleniti atque corrupti quos do.</p>
  <div class="c-foot"><span class="avatar" role="img" aria-label="Reviewer photo"></span><span class="c-name">Tessa Vale</span><span class="c-date">28 Feb 2019</span></div></div>

<!-- footer -->
<svg class="abs footer-curve" viewBox="0 0 1200 681" preserveAspectRatio="none">
  <path fill="#00a990" d="M0 150 C300 60 700 20 1200 40 L1200 70 C800 70 400 120 0 210 Z"/>
  <path fill="#0b2a6e" d="M0 200 C400 110 800 60 1200 60 L1200 681 L0 681 Z"/>
</svg>
<div class="abs f-brand"><span class="brand-mark"></span><span class="brand-name">SAIL US TO HARBOURLIGHT</span></div>

<h3 class="f-h" style="left:150px;top:4945px">Sign up for newsletter</h3>
<p class="f-text" style="left:150px;top:4996px;width:300px">Excepteur sint occaecat cupidatat non proident, sunt in culpa qui officia deserunt</p>
<div class="abs email-field">Enter email</div>
<div class="abs btn-signup">SIGN UP</div>

<h3 class="f-h" style="left:562px;top:4945px">Quick Links</h3>
<ul class="abs links">
  <li>Destinations</li><li>Tours</li><li>Documentary</li><li>Special Offers</li><li>About Us</li><li>Before You Go</li><li>Reviews</li>
</ul>

<h3 class="f-h" style="left:833px;top:4945px">Contact Us</h3>
<div class="contact-row" style="top:5006px"><span class="c-icon"><svg width="14" height="18" viewBox="0 0 14 18"><path fill="#fff" d="M7 0a7 7 0 0 0-7 7c0 5 7 11 7 11s7-6 7-11a7 7 0 0 0-7-7zm0 9.5A2.5 2.5 0 1 1 7 4.5a2.5 2.5 0 0 1 0 5z"/></svg></span>
  <span>Harbourlight House<br>27 Tidewater Lane,<br>Nelson 7010</span></div>
<div class="contact-row" style="top:5086px"><span class="c-icon"><svg width="16" height="16" viewBox="0 0 24 24"><path fill="#fff" d="M6.6 10.8a15 15 0 0 0 6.6 6.6l2.2-2.2a1 1 0 0 1 1-.25 11.4 11.4 0 0 0 3.6.57 1 1 0 0 1 1 1V20a1 1 0 0 1-1 1A17 17 0 0 1 3 4a1 1 0 0 1 1-1h3.5a1 1 0 0 1 1 1c0 1.25.2 2.45.57 3.6a1 1 0 0 1-.25 1z"/></svg></span>
  <span>Call us today:<br>(555) 014-2286</span></div>
<div class="contact-row" style="top:5146px"><span class="c-icon"><svg width="16" height="12" viewBox="0 0 16 12"><rect x="0.5" y="0.5" width="15" height="11" fill="none" stroke="#fff"/><path d="M0.5 0.5 L8 7 L15.5 0.5" fill="none" stroke="#fff"/></svg></span>
  <span>Email :<br>sailustoharbourlightnz@quillmail.example</span></div>

<div class="abs foot-social"><span class="s1"></span><span class="s2"></span><span class="s3"></span><span class="s4"></span><span class="s5"></span></div>
<div class="abs copy">© Copyright 2019 The Company name. All Rights Reserved.</div>

</body>
</html>
```